VELNUKA Promotions - Business Card Design Project

We are looking for a classy business cards for Promotion Company based in Toronto, Canada named Velnuka Promotions.

Velnuka Promotions has an idea and vision to set high standard, be EXCLUSIVE and attract a group of people that will follow us through events we promote (night clubs, brand promotions, music events, and sport events)

We want to present a high standards and classy image to the others...
Updates

Target Market(s)

male/female age 25-40 Target: business owners young entrepreneur - clubing industry - media industry - promotion industry - marketing media industry

Industry/Entity Type

Events

Requirements
Must have
• business cards should be classy, make people feel exclusive , make people react ..

```html
<!DOCTYPE html>
<html lang="en">
<head>
<meta charset="utf-8">
<title>Velnuka Promotions – Business Cards</title>
<link rel="stylesheet" href="https://fonts.googleapis.com/css2?family=Cinzel:wght@400;500&family=Didact+Gothic&display=swap">
<style>
  :root {
    --stage: #e9e6e1;
    --card-black: #000000;
    --brand-cyan: #00b3ea;
    --logo-cyan: #1fb6e8;
    --white: #ffffff;
    --sky-light: #c9c9c9;
    --sky-mid: #8a8a8a;
    --sky-dark: #3a3a3a;
    --card-shadow: 0 10px 24px rgba(0,0,0,0.35);
  }
  html, body {
    margin: 0;
    padding: 0;
    width: 1200px;
    height: 1139px;
    overflow: hidden;
    background: var(--stage);
  }
  .canvas {
    position: relative;
    width: 1200px;
    height: 1139px;
  }
  .card {
    position: absolute;
    width: 752px;
    height: 431px;
    box-shadow: var(--card-shadow);
    overflow: hidden;
  }
  /* Front */
  .card--front {
    left: 68px;
    top: 53px;
    background: var(--card-black);
  }
  .skyline-photo {
    position: absolute;
    inset: 0;
    background:
      linear-gradient(180deg, var(--sky-mid) 0%, var(--sky-light) 22%, var(--sky-mid) 45%, var(--sky-dark) 70%, #1c1c1c 100%);
  }
  .front-band {
    position: absolute;
    left: 0;
    top: 0;
    width: 752px;
    height: 431px;
  }
  .front-logo {
    position: absolute;
    left: 122px;
    top: 300px;
    width: 545px;
    text-align: right;
  }
  .front-logo__name {
    display: block;
    font-family: "Cinzel", serif;
    font-weight: 400;
    font-size: 78px;
    line-height: 1;
    letter-spacing: 1px;
    color: var(--logo-cyan);
  }
  .front-logo__tagline {
    display: block;
    margin-top: 6px;
    font-family: "Cinzel", serif;
    font-weight: 500;
    font-size: 22px;
    letter-spacing: 7px;
    color: var(--white);
  }
  /* Back */
  .card--back {
    left: 387px;
    top: 551px;
    background: var(--brand-cyan);
  }
  .back-logo {
    position: absolute;
    right: 56px;
    top: 48px;
    text-align: right;
  }
  .back-logo__name {
    display: block;
    font-family: "Cinzel", serif;
    font-size: 38px;
    line-height: 1;
    color: var(--white);
  }
  .back-logo__tagline {
    display: block;
    margin-top: 2px;
    font-family: "Cinzel", serif;
    font-size: 11px;
    letter-spacing: 4px;
    color: var(--white);
  }
  .contact-line {
    position: absolute;
    left: 35px;
    right: 35px;
    top: 382px;
    margin: 0;
    padding: 0;
    list-style: none;
    font-family: "Didact Gothic", sans-serif;
    font-size: 19px;
    color: var(--white);
  }
  .contact-line li {
    position: absolute;
    top: 0;
    white-space: nowrap;
  }
  .contact-line__email { left: 0; }
  .contact-line__address { left: 270px; }
  .contact-line__phone { left: 505px; }
</style>
</head>
<body>
<main class="canvas">
  <section class="card card--front" aria-label="Business card front">
    <div class="skyline-photo" role="img" aria-label="Black and white photograph of a city skyline under a cloudy sky with a light floral ornament"></div>
    <svg class="front-band" viewBox="0 0 752 431" aria-hidden="true">
      <path d="M0,312 C40,282 90,276 140,296 C170,306 200,300 240,296 L560,296 C640,296 700,282 752,250 L752,431 L0,431 Z" fill="var(--card-black)"/>
    </svg>
    <div class="front-logo">
      <span class="front-logo__name">VELNUKA</span>
      <span class="front-logo__tagline">PROMOTIONS</span>
    </div>
  </section>

  <section class="card card--back" aria-label="Business card back">
    <div class="back-logo">
      <span class="back-logo__name">VELNUKA</span>
      <span class="back-logo__tagline">PROMOTIONS</span>
    </div>
    <ul class="contact-line">
      <li class="contact-line__email">name@velnuka.com</li>
      <li class="contact-line__address">1 street, town, code</li>
      <li class="contact-line__phone">+27 82 555 0142</li>
    </ul>
  </section>
</main>
</body>
</html>
```